Talvok Engineering Business card Design

We need to make business cards for our NDT and inspection company. The company is called Talvok Engineering. We want a professional modern feel business card. We have just completed the remaking of our website and would like to have business cards with the same feel and colours. The final design should communicate professionalism and cutting edge tech.

Target Market(s)

We sell to B2B Business clients. Our customer is an engineer or decision maker in the mechanical engineering / Oil and gas field.

Contact Information for Business Card

Please see the current business cards that we have uploaded to get the details. You can also look at our Website www.talvok-eng.example for more.

Requirements
Must have
• Less is more
Nice to have
• Less is more

```html
<!DOCTYPE html>
<html lang="en">
<head>
<meta charset="utf-8">
<title>Talvok Engineering – Business Card</title>
<link href="https://fonts.googleapis.com/css2?family=Roboto:wght@400;500;700&display=swap" rel="stylesheet">
<style>
  :root {
    --page-bg: #0d0d0d;
    --card-bg: #2b2b2d;
    --card-edge: #b3121b;
    --text-light: #f2f2f2;
    --text-muted: #c9c9c9;
    --rule: #6a6a6a;
    --brand-blue: #1f3a8a;
    --brand-red: #b3121b;
    --emboss: #444447;
    --emboss-text: #5a5a5d;
  }
  * { box-sizing: border-box; margin: 0; padding: 0; }
  html, body { width: 1200px; height: 822px; overflow: hidden; background: var(--page-bg); }
  body { font-family: "Roboto", Arial, sans-serif; position: relative; }

  .card {
    position: absolute;
    top: 261px;
    width: 525px;
    height: 300px;
    background: var(--card-bg);
    border-bottom: 4px solid var(--card-edge);
    border-right: 2px solid var(--card-edge);
    box-shadow: 0 20px 40px rgba(0,0,0,.6);
    color: var(--text-light);
  }
  .card--front { left: 50px; }
  .card--back  { left: 625px; }

  /* Front */
  .brand {
    position: absolute; top: 48px; left: 150px;
    display: flex; align-items: center; gap: 18px;
  }
  .brand__dot {
    width: 64px; height: 64px; border-radius: 50%;
    background: var(--brand-red);
  }
  .brand__divider { width: 1px; height: 60px; background: var(--rule); }
  .brand__name {
    font-weight: 700; font-size: 26px; line-height: 1.05;
    color: var(--brand-blue); letter-spacing: 1px; text-transform: uppercase;
  }
  .front-rule {
    position: absolute; top: 150px; left: 30px; right: 95px;
    height: 1px; background: var(--rule);
  }
  .social { position: absolute; top: 140px; right: 40px; display: flex; gap: 6px; }
  .social__dot { width: 20px; height: 20px; border-radius: 50%; background: var(--text-light); }

  .person { position: absolute; top: 168px; left: 30px; }
  .person__name { font-weight: 700; font-size: 17px; letter-spacing: .5px; }
  .person__role { font-size: 13px; color: var(--text-muted); margin-top: 2px; }

  .contact { position: absolute; bottom: 22px; left: 30px; list-style: none; font-size: 13px; line-height: 19px; }
  .contact li { display: flex; align-items: center; gap: 7px; }
  .contact svg { width: 13px; height: 13px; flex: none; }

  .address {
    position: absolute; bottom: 60px; right: 30px;
    text-align: right; font-size: 13px; line-height: 18px;
  }

  /* Back */
  .services { position: absolute; list-style: none; font-size: 12.5px; line-height: 17px; color: var(--text-muted); }
  .services li::before { content: "• "; color: var(--text-light); }
  .services--main { top: 80px; left: 32px; }
  .services--ndt { top: 26px; left: 330px; }
  .services--projects { top: 116px; left: 345px; }
  .back-brand {
    position: absolute; bottom: 42px; right: 34px;
    display: flex; align-items: center; gap: 16px;
  }
  .back-brand__dot { width: 78px; height: 78px; border-radius: 50%; background: var(--emboss); }
  .back-brand__divider { width: 1px; height: 62px; background: var(--emboss); }
  .back-brand__name {
    font-weight: 700; font-size: 26px; line-height: 1.05;
    color: var(--emboss-text); text-transform: uppercase; letter-spacing: 1px;
  }
</style>
</head>
<body>

<section class="card card--front" aria-label="Business card front">
  <div class="brand">
    <span class="brand__dot"></span>
    <span class="brand__divider"></span>
    <span class="brand__name">Talvok<br>Engineering</span>
  </div>
  <div class="front-rule"></div>
  <div class="social"><span class="social__dot"></span><span class="social__dot"></span></div>

  <div class="person">
    <p class="person__name">DANIEL OKORO</p>
    <p class="person__role">Managing Director</p>
  </div>

  <ul class="contact">
    <li>
      <svg viewBox="0 0 16 16" fill="none" stroke="currentColor" stroke-width="1.4"><rect x="1" y="1" width="14" height="14" rx="2"/><path d="M5 4l2 2-1 1.5c.8 1.5 1.7 2.4 3 3L10.5 9.5l2 2-1.5 1.5C7 12.5 3.5 9 3 5z"/></svg>
      + 254 20 555 0142/3
    </li>
    <li>
      <svg viewBox="0 0 16 16" fill="none" stroke="currentColor" stroke-width="1.4"><rect x="1" y="3" width="14" height="10"/><path d="M1 3l7 6 7-6"/></svg>
      info@talvok-eng.example
    </li>
    <li>
      <svg viewBox="0 0 16 16" fill="none" stroke="currentColor" stroke-width="1.2"><circle cx="8" cy="8" r="7"/><ellipse cx="8" cy="8" rx="3" ry="7"/><path d="M1 8h14M2.5 4.5h11M2.5 11.5h11"/></svg>
      www.talvok-eng.example
    </li>
  </ul>

  <p class="address">P.O. BOX 40518-80100<br>Mombasa, Kenya</p>
</section>

<section class="card card--back" aria-label="Business card back">
  <ul class="services services--main">
    <li>API 653 Tank Inspections</li>
    <li>API 570 Pipeline Inspections</li>
    <li>API 510 Pressure Vessel Inspections</li>
    <li>Welding Inspection</li>
    <li>Electrical Inspection</li>
    <li>OCTG Inspections</li>
    <li>Lifting Equipment Inspections</li>
  </ul>
  <ul class="services services--ndt">
    <li>Non-Destructive Testing</li>
    <li>UT/PT/MT/RT/VT</li>
    <li>Advanced NDT</li>
    <li>PAUT/MFL/ILI</li>
  </ul>
  <ul class="services services--projects">
    <li>Engineering Projects</li>
  </ul>
  <div class="back-brand">
    <span class="back-brand__dot"></span>
    <span class="back-brand__divider"></span>
    <span class="back-brand__name">Talvok<br>Engineering</span>
  </div>
</section>

</body>
</html>
```